I need a luxury/high-end real estate looking website for my Vending business

Hello & thank you in advance for your time spent on this project.

I have a vending business (Copper Lantern Vending Services) based here in downtown Miami & my clients are high-end/luxury buildings throughout the area.
We offer free placement of 5 vending machine options (snacks, drinks, laundry products, healthy options or combo machine) to high traffic locations.

The goal of this website is to be a lead generator. So having an inquiry form on the top of the page is key.

Aesthetically, I want the website to feel like a high-end commercial real estate website. We service luxury buildings, so I want that look of the downtown skyline mixed in with the vending machine images throughout the site.

On the main page, it would be :
*the inquiry form (name of location, # of machines, machine option, contact info)
*What we do section - vending machine placement, bi-weekly or monthly refill service & ongoing customer support.
*5 vending machine options section - (with clickable images to see what all products you can have the machine filled with)
*reviews section
*social feed or blog post section
*about us section
then of course the contact info etc at the bottom of page

For the question ''how many pages do you need designed'', I answered 5+, which is in reference to the main page outlined above plus the 5 clickable images that takes you to the product options. I'm assuming the clickable images would be pages on their own.

Target Market(s)

High traffic businesses & residences in downtown Miami

Industry/Entity Type

Vending Machines

Coding

Coded - Design and coding required

Number of Pages Required

5+ page

Requirements
Must have
• Inquiry form
Nice to have
• To have a feel of a luxury/high-end commercial real estate website

```html
<!DOCTYPE html>
<html lang="en">
<head>
<meta charset="UTF-8">
<title>Copper Lantern Vending Services</title>
<link href="https://fonts.googleapis.com/css2?family=Oswald:wght@500;600&family=Roboto:wght@400;500;700&display=swap" rel="stylesheet">
<style>
:root{
  --red:#e3230f;
  --red-dark:#c81a0a;
  --ink:#1f1f1f;
  --text:#6e6e6e;
  --muted:#9a9a9a;
  --light:#f4f4f4;
  --line:#e2e2e2;
  --footer:#1d1d1d;
  --white:#ffffff;
}
*{margin:0;padding:0;box-sizing:border-box}
html,body{width:1200px;height:4242px;overflow:hidden}
body{font-family:"Roboto",Arial,sans-serif;color:var(--ink);background:var(--white);position:relative}
.abs{position:absolute}
.heading{font-family:"Oswald",Arial,sans-serif;font-weight:600;text-transform:uppercase;color:var(--ink)}
.section-title{position:absolute;left:0;width:1200px;text-align:center;font-size:40px;line-height:1}
.underline{position:absolute;height:3px;width:92px;background:var(--red)}
.btn{position:absolute;background:var(--red);color:#fff;font-size:13px;font-weight:700;text-transform:uppercase;border-radius:22px;display:flex;align-items:center;justify-content:center}

/* header */
.site-header{position:absolute;top:0;left:0;width:1200px;height:118px;background:#fff}
.brand{position:absolute;left:110px;top:32px;font-family:"Oswald",sans-serif;font-weight:600;font-size:21px;line-height:27px;text-transform:uppercase;color:var(--ink)}
.brand .accent{color:var(--red)}
.topbar{position:absolute;top:18px;left:640px;height:20px;display:flex;align-items:center;font-size:13px;color:#333}
.topbar .sep{margin:0 14px;color:#999}
.topbar svg{margin-right:8px}
.socials-top{position:absolute;top:15px;left:957px;display:flex;gap:5px}
.soc{width:28px;height:28px;border-radius:50%;border:1.5px solid #d8d8d8;background:#fff}
.soc.fill{background:var(--red);border-color:var(--red)}
.nav-rule{position:absolute;left:476px;top:59px;width:614px;height:1px;background:var(--line)}
.nav{position:absolute;top:80px;left:476px;width:614px;display:flex;justify-content:space-between;font-size:14px;font-weight:500;text-transform:uppercase}
.nav .active{position:relative}
.nav .active::after{content:"";position:absolute;left:0;right:0;bottom:-8px;height:2px;background:var(--red)}

/* hero */
.hero{position:absolute;top:118px;left:0;width:1200px;height:598px;background:linear-gradient(90deg,#3a3836 0%,#5f5a55 30%,#8c8580 48%,#5e5853 70%,#2e2c2a 100%)}
.hero-photo{position:absolute;inset:0;background:radial-gradient(ellipse 260px 360px at 520px 300px,rgba(220,214,206,.45),transparent 70%)}
.hero-title{position:absolute;left:110px;top:183px;color:#fff;font-size:40px;line-height:46px}
.hero-copy{position:absolute;left:110px;top:291px;width:430px;color:#fff;font-size:18px;line-height:28px}
.inquiry{position:absolute;left:736px;top:103px;width:354px;height:405px;background:rgba(255,255,255,.25);border-radius:8px}
.inquiry-card{position:absolute;left:10px;top:10px;width:334px;height:385px;background:#fff;border-radius:6px}
.inquiry-card h2{position:absolute;top:36px;left:0;width:100%;text-align:center;font-size:24px}
.field{position:absolute;height:36px;border:1px solid #ececec;border-radius:18px;background:#f7f7f7;font-size:12px;color:#888;display:flex;align-items:center;padding-left:18px;box-shadow:inset 0 1px 2px rgba(0,0,0,.04)}
.field .chev{position:absolute;right:16px;top:13px}

/* categories */
.categories{position:absolute;top:716px;left:0;width:1200px;height:712px;background:var(--light)}
.cat-card{position:absolute;top:192px;width:306px;height:402px;background:#fff;border-radius:4px;box-shadow:0 2px 10px rgba(0,0,0,.08)}
.cat-card.active{border:2px solid var(--red)}
.cat-photo{position:absolute;left:74px;top:38px;width:158px;height:158px;border-radius:50%}
.cat-name{position:absolute;top:230px;left:0;width:100%;text-align:center;font-size:17px;font-weight:500;text-transform:uppercase}
.cat-text{position:absolute;top:264px;left:20px;right:20px;text-align:center;font-size:13.5px;line-height:26px;color:var(--text)}
.slider-arrow{position:absolute;width:34px;height:34px;border-radius:50%;background:#d6d6d6;display:flex;align-items:center;justify-content:center}
.card-arrow{position:absolute;left:582px;top:1292px;width:36px;height:36px;border-radius:50%;background:var(--red);display:flex;align-items:center;justify-content:center}

/* about */
.about-photo{position:absolute;left:110px;top:1559px;width:489px;height:375px;background:linear-gradient(120deg,#6d6a66 0%,#b8b0a6 40%,#4c5560 70%,#2d2f33 100%)}
.about-title{position:absolute;left:665px;top:1584px;font-size:40px;line-height:1}
.about-copy{position:absolute;left:665px;top:1672px;width:425px;font-size:14px;line-height:25.5px;color:var(--text)}

/* how it works */
.how{position:absolute;top:2061px;left:0;width:1200px;height:523px;background:linear-gradient(90deg,#d8321f 0%,#e8412a 50%,#e1351f 100%)}
.how .section-title{color:#fff;top:74px}
.step-circle{position:absolute;top:176px;width:123px;height:123px;border-radius:50%;background:#fff;display:flex;align-items:center;justify-content:center}
.step-name{position:absolute;top:336px;width:300px;text-align:center;color:#fff;font-size:16px;font-weight:700;text-transform:uppercase}
.step-text{position:absolute;top:373px;width:300px;text-align:center;color:#fff;font-size:13.5px;line-height:25.5px}

/* testimonials */
.avatar{position:absolute;left:538px;top:2770px;width:123px;height:123px;border-radius:50%;background:linear-gradient(160deg,#9aa598,#5d6a5a 55%,#3f4a3e)}
.quote-badge{position:absolute;left:631px;top:2768px;width:30px;height:30px;border-radius:50%;background:var(--red);display:flex;align-items:center;justify-content:center}
.testi-copy{position:absolute;left:160px;top:2917px;width:880px;text-align:center;font-size:14px;line-height:26px;color:var(--text)}
.stars{position:absolute;left:0;width:1200px;top:3006px;display:flex;justify-content:center;gap:4px}
.testi-name{position:absolute;left:0;width:1200px;top:3040px;text-align:center;font-size:20px;font-weight:500}
.testi-name span{font-size:14px;font-weight:400}

/* blog */
.blog{position:absolute;top:3150px;left:0;width:1200px;height:705px;background:var(--light)}
.post{position:absolute;background:#fff;box-shadow:0 2px 10px rgba(0,0,0,.07)}
.post-photo{position:absolute}
.post-date{position:absolute;display:flex;align-items:center;gap:10px;font-size:11px;color:#444}
.post-date i{display:block;width:24px;height:24px;border-radius:50%;background:#e6e6e6}
.post-title{position:absolute;font-size:16px;font-weight:500;line-height:24px;text-transform:uppercase}
.post-text{position:absolute;font-size:13px;line-height:22px;color:var(--text)}
.read-more{position:absolute;font-size:12px;font-weight:700;color:var(--red);text-decoration:underline;text-transform:uppercase}

/* footer */
.site-footer{position:absolute;top:3855px;left:0;width:1200px;height:387px;background:var(--footer);color:#fff}
.foot-brand{position:absolute;left:110px;top:162px;font-family:"Oswald",sans-serif;font-weight:600;font-size:21px;line-height:27px;text-transform:uppercase}
.foot-brand .accent{color:var(--red)}
.foot-divider{position:absolute;top:58px;width:2px;height:120px;background:var(--red)}
.foot-divider.grey{top:178px;height:110px;width:1px;background:#444}
.foot-head{position:absolute;top:72px;font-size:15px;font-weight:700;text-transform:uppercase}
.quick-links{position:absolute;left:364px;top:112px;list-style:none;font-size:14px}
.quick-links li{height:38px;position:relative;padding-left:37px}
.quick-links li::before{content:"»";position:absolute;left:0;top:-2px;color:var(--red);font-size:15px}
.contact-item{position:absolute;left:573px;width:190px}
.contact-item svg{position:absolute;left:0;top:2px}
.contact-item .label{padding-left:38px;font-size:14px;font-weight:700;text-transform:uppercase}
.contact-item .val{padding-left:38px;font-size:11px;line-height:18px;margin-top:6px}
.newsletter{position:absolute;left:805px;top:115px;width:283px;height:47px;border-radius:24px;background:#fff;border:2px solid #fff}
.newsletter span{position:absolute;left:16px;top:14px;font-size:13px;color:#666}
.newsletter b{position:absolute;right:0;top:0;width:106px;height:43px;border-radius:22px;background:var(--red);color:#fff;font-size:13px;display:flex;align-items:center;justify-content:center}
.foot-socials{position:absolute;left:805px;top:185px;display:flex;gap:7px}
.foot-socials .soc{width:36px;height:36px;border:1.5px solid #fff;background:transparent}
.foot-socials .soc.fill{background:var(--red);border-color:var(--red)}
.foot-rule{position:absolute;left:110px;top:314px;width:980px;height:1px;background:#3c3c3c}
.copyright{position:absolute;left:0;width:1200px;top:344px;text-align:center;font-size:12px}
.chat{position:absolute;left:1117px;top:278px;width:44px;height:44px;border-radius:50%;background:var(--red);display:flex;align-items:center;justify-content:center}
</style>
</head>
<body>

<header class="site-header">
  <div class="brand">Copper Lantern<br><span class="accent">Vending Services</span></div>
  <div class="topbar">
    <svg width="12" height="12" viewBox="0 0 24 24"><path fill="#e3230f" d="M6.6 10.8a15.1 15.1 0 0 0 6.6 6.6l2.2-2.2c.3-.3.7-.4 1-.2 1.1.4 2.3.6 3.6.6.6 0 1 .4 1 1V20c0 .6-.4 1-1 1A17 17 0 0 1 3 4c0-.6.4-1 1-1h3.5c.6 0 1 .4 1 1 0 1.3.2 2.5.6 3.6.1.3 0 .7-.2 1z"/></svg>
    +1 (305) 555 0142<span class="sep">|</span>
    <svg width="13" height="11" viewBox="0 0 24 18"><rect width="24" height="18" rx="2" fill="#e3230f"/><path d="M2 3l10 7 10-7" stroke="#fff" stroke-width="2" fill="none"/></svg>
    info@copperlantern.co
  </div>
  <div class="socials-top"><div class="soc fill"></div><div class="soc"></div><div class="soc"></div><div class="soc"></div></div>
  <div class="nav-rule"></div>
  <nav class="nav">
    <span class="active">Home</span><span>About Us</span>
    <span>Vending Machines <svg width="9" height="6" viewBox="0 0 10 6"><path d="M1 1l4 4 4-4" stroke="#333" stroke-width="1.5" fill="none"/></svg></span>
    <span>Resources</span><span>Contact Us</span>
  </nav>
</header>

<section class="hero">
  <div class="hero-photo" role="img" aria-label="Woman in a striped blazer selecting a product at a vending machine"></div>
  <h1 class="heading hero-title">Copper Lantern<br>Vending Services</h1>
  <p class="hero-copy">Lorem ipsum dolor sit amet, consectetur adipiscin elit, sed do eiusmod tempor.</p>
  <div class="btn" style="left:110px;top:371px;width:134px;height:39px">Learn More</div>

  <div class="inquiry">
    <div class="inquiry-card">
      <h2 class="heading">Inquiry Form</h2>
      <div class="underline" style="left:145px;top:76px;width:44px"></div>
      <div class="field" style="left:34px;top:96px;width:266px">Your Name</div>
      <div class="field" style="left:34px;top:147px;width:133px;border-radius:18px 0 0 18px">Phone</div>
      <div class="field" style="left:167px;top:147px;width:133px;border-radius:0 18px 18px 0;padding-left:12px">Email</div>
      <div class="field" style="left:34px;top:198px;width:266px">No.of Machines<svg class="chev" width="9" height="6" viewBox="0 0 10 6"><path d="M1 1l4 4 4-4" stroke="#777" stroke-width="1.5" fill="none"/></svg></div>
      <div class="field" style="left:34px;top:249px;width:266px">Category<svg class="chev" width="9" height="6" viewBox="0 0 10 6"><path d="M1 1l4 4 4-4" stroke="#777" stroke-width="1.5" fill="none"/></svg></div>
      <div class="btn" style="left:34px;top:307px;width:266px;height:39px">Submit</div>
    </div>
  </div>
</section>

<section class="categories">
  <h2 class="heading section-title" style="top:79px">Vending Machine Categories</h2>
  <div class="underline" style="left:554px;top:128px"></div>
  <div class="slider-arrow" style="left:39px;top:375px"><svg width="8" height="12" viewBox="0 0 8 12"><path d="M6 1L1 6l5 5" stroke="#fff" stroke-width="2" fill="none"/></svg></div>
  <div class="slider-arrow" style="left:1125px;top:375px"><svg width="8" height="12" viewBox="0 0 8 12"><path d="M2 1l5 5-5 5" stroke="#fff" stroke-width="2" fill="none"/></svg></div>

  <div class="cat-card" style="left:110px">
    <div class="cat-photo" role="img" aria-label="Person taking a snack from a vending machine" style="background:linear-gradient(135deg,#c9c3bb,#8c8a87 50%,#d8d2cb)"></div>
    <div class="cat-name">Snacks</div>
    <p class="cat-text">Lorem ipsum dolor sit amet, consectetur adipiscing elit, sed do eiusmod tempor incididunt ut labore et dolore magna aliq m ad minim veniam.</p>
  </div>
  <div class="cat-card active" style="left:447px">
    <div class="cat-photo" role="img" aria-label="Shelves of bottled drinks inside a machine" style="left:72px;top:36px;background:linear-gradient(135deg,#4a3a28,#b58a3c 45%,#e1b54a 60%,#3b3026)"></div>
    <div class="cat-name" style="top:228px">Drinks</div>
    <p class="cat-text" style="top:262px">Lorem ipsum dolor sit amet, consectetur adipiscing elit, sed do eiusmod tempor incididunt ut labore et dolore magna aliq m ad minim veniam.</p>
  </div>
  <div class="cat-card" style="left:784px">
    <div class="cat-photo" role="img" aria-label="Front of a laundry products vending machine" style="background:linear-gradient(160deg,#8b98a6,#c7ccd2 45%,#6c7079)"></div>
    <div class="cat-name">Laundry Products</div>
    <p class="cat-text">Lorem ipsum dolor sit amet, consectetur adipiscing elit, sed do eiusmod tempor incididunt ut labore et dolore magna aliq m ad minim veniam.</p>
  </div>
</section>
<div class="card-arrow"><svg width="9" height="13" viewBox="0 0 8 12"><path d="M2 1l5 5-5 5" stroke="#fff" stroke-width="2" fill="none"/></svg></div>

<section>
  <div class="about-photo" role="img" aria-label="Student with a backpack choosing items from a vending machine"></div>
  <h2 class="heading about-title">About Us</h2>
  <div class="underline" style="left:665px;top:1635px;width:76px"></div>
  <p class="about-copy">Lorem ipsum dolor sit amet, consectetur adipiscing elit, sed do eiusmod tempor incididunt ut labore et dolore magna aliqua. Ut enim ad minim veniam, quis nostrud exercitation ullamco laboris nisi ut aliquip ex ea commodo consequat. Duis aute irure dolor in reprehenderit in voluptate velit esse cillum dolore eu fugiat nulla pariatu pteur sint occaecat .</p>
  <div class="btn" style="left:665px;top:1862px;width:134px;height:42px">Learn More</div>
</section>

<section class="how">
  <h2 class="heading section-title">How It Works</h2>
  <div class="underline" style="left:566px;top:124px;width:68px;background:#fff"></div>
  <svg class="abs" style="left:340px;top:222px" width="170" height="60" viewBox="0 0 170 60"><path d="M5 50 Q85 75 150 20" stroke="rgba(255,255,255,.3)" stroke-width="8" fill="none"/><path d="M138 14 L160 12 L152 32 Z" fill="rgba(255,255,255,.3)"/></svg>
  <svg class="abs" style="left:690px;top:175px" width="170" height="60" viewBox="0 0 170 60"><path d="M5 40 Q80 -5 150 35" stroke="rgba(255,255,255,.3)" stroke-width="8" fill="none"/><path d="M140 22 L160 42 L136 46 Z" fill="rgba(255,255,255,.3)"/></svg>

  <div class="step-circle" style="left:196px">
    <svg width="70" height="56" viewBox="0 0 70 56" fill="none" stroke="#222" stroke-width="2.4"><circle cx="20" cy="34" r="16"/><path d="M20 25v18M24 28c-2-2-8-2-8 2s8 2 8 6-6 4-8 2"/><ellipse cx="48" cy="12" rx="14" ry="5"/><path d="M34 12v8c0 3 6 5 14 5s14-2 14-5v-8"/><path d="M36 25c1 2 6 4 12 4s14-2 14-5v-4"/><path d="M38 36c2 1 5 2 10 2 8 0 14-2 14-5v-9M38 46c2 1 5 2 10 2 8 0 14-2 14-5v-10"/></svg>
  </div>
  <div class="step-circle" style="left:538px">
    <svg width="64" height="60" viewBox="0 0 64 60" fill="none" stroke="#222" stroke-width="2.4"><circle cx="38" cy="24" r="15"/><circle cx="38" cy="24" r="6"/><path d="M38 4v5M38 39v5M18 24h5M53 24h5M24 10l4 4M48 34l4 4M24 38l4-4M48 14l4-4"/><circle cx="16" cy="44" r="9"/><circle cx="16" cy="44" r="3"/><path d="M16 31v4M16 53v4M3 44h4M25 44h4"/></svg>
  </div>
  <div class="step-circle" style="left:880px">
    <svg width="50" height="66" viewBox="0 0 50 66" fill="none" stroke="#222" stroke-width="2.4"><rect x="3" y="2" width="44" height="62" rx="3"/><rect x="9" y="8" width="32" height="30"/><path d="M9 18h32M9 28h32M20 8v30M31 8v30"/><circle cx="14" cy="50" r="3"/><circle cx="22" cy="50" r="3"/><path d="M30 46h10v8H30z"/></svg>
  </div>
  <div class="step-name" style="left:107px">Lorem Ipsum Dolor</div>
  <div class="step-name" style="left:449px">Lorem Ipsum Dolor</div>
  <div class="step-name" style="left:791px">Lorem Ipsum Dolor</div>
  <p class="step-text" style="left:107px">Lorem ipsum dolor sit amet, consectetur adipiscing elit, sed do eiusmod tempor incididunt labore dolorea.</p>
  <p class="step-text" style="left:449px">Lorem ipsum dolor sit amet, consectetur adipiscing elit, sed do eiusmod tempor incididunt labore dolorea.</p>
  <p class="step-text" style="left:791px">Lorem ipsum dolor sit amet, consectetur adipiscing elit, sed do eiusmod tempor incididunt labore dolorea.</p>
</section>

<section>
  <h2 class="heading section-title" style="top:2680px">Testimonials</h2>
  <div class="underline" style="left:563px;top:2729px;width:74px"></div>
  <div class="avatar" role="img" aria-label="Portrait of a smiling client"></div>
  <div class="quote-badge"><svg width="13" height="10" viewBox="0 0 14 10" fill="#fff"><path d="M0 10V6C0 2 2 0 5 0v2C3 2 2.5 3.5 2.5 5H5v5zM8 10V6c0-4 2-6 5-6v2c-2 0-2.5 1.5-2.5 3H13v5z"/></svg></div>
  <svg class="abs" style="left:99px;top:2945px" width="12" height="22" viewBox="0 0 12 22"><path d="M10 2L2 11l8 9" stroke="#bbb" stroke-width="2" fill="none"/></svg>
  <svg class="abs" style="left:1088px;top:2945px" width="12" height="22" viewBox="0 0 12 22"><path d="M2 2l8 9-8 9" stroke="#222" stroke-width="2.2" fill="none"/></svg>
  <p class="testi-copy">Lorem ipsum dolor sit amet, consectetur adipiscing elit, sed do eiusmod tempor incididunt ut labore et dolore magna aliqua. Ut enim ad minim veniam, quis nostrud exercitation ullamco laboris nisi ut aliquip ex ea commodo consequat. Duis aute irure dolor in reprehenderit in voluptate velit esse cillum dolore eu fugiat nulla pariatur.</p>
  <div class="stars">
    <svg width="84" height="16" viewBox="0 0 84 16" fill="#e3230f"><path id="s" d="M8 0l2.4 5 5.6.7-4.1 3.8 1 5.5L8 12.4 3.1 15l1-5.5L0 5.7 5.6 5z"/><use href="#s" x="17"/><use href="#s" x="34"/><use href="#s" x="51"/><use href="#s" x="68"/></svg>
  </div>
  <div class="testi-name">MARCUS DELGADO, <span>United States</span></div>
</section>

<section class="blog">
  <h2 class="heading section-title" style="top:80px">Latest Blog Post</h2>
  <div class="underline" style="left:563px;top:129px;width:74px"></div>

  <article class="post" style="left:110px;top:177px;width:481px;height:446px">
    <div class="post-photo" role="img" aria-label="Couple choosing snacks at a vending machine" style="left:9px;top:9px;width:463px;height:282px;background:linear-gradient(120deg,#5a5550,#a49a8e 40%,#d5cbbd 55%,#3c3a38)"></div>
    <div class="post-date" style="left:30px;top:305px"><i></i>April 1, 2022</div>
    <h3 class="post-title" style="left:30px;top:344px;width:420px">Lorem ipsum dolor sit amet, consectetur adipiscing elit, sed do eius</h3>
    <span class="read-more" style="left:30px;top:404px">Read More</span>
  </article>

  <article class="post" style="left:609px;top:177px;width:479px;height:214px">
    <div class="post-photo" role="img" aria-label="Hand inserting a coin into a vending machine slot" style="left:8px;top:8px;width:196px;height:198px;background:linear-gradient(135deg,#2f2f33,#8c8a88 50%,#d9d4cd)"></div>
    <div class="post-date" style="left:226px;top:24px"><i></i>April 1, 2022</div>
    <h3 class="post-title" style="left:226px;top:62px;width:230px">Lorem ipsum dolor sit amet, consec</h3>
    <p class="post-text" style="left:226px;top:118px;width:240px">Lorem ipsum dolor sit amet, consec tetur adipiscing elit.</p>
    <span class="read-more" style="left:226px;top:176px">Read More</span>
  </article>

  <article class="post" style="left:609px;top:409px;width:479px;height:214px">
    <div class="post-photo" role="img" aria-label="Friends laughing beside a vending machine" style="left:8px;top:8px;width:196px;height:198px;background:linear-gradient(135deg,#8e8578,#cfc3b3 45%,#5c5650)"></div>
    <div class="post-date" style="left:226px;top:24px"><i></i>April 1, 2022</div>
    <h3 class="post-title" style="left:226px;top:62px;width:230px">Lorem ipsum dolor sit amet, consec</h3>
    <p class="post-text" style="left:226px;top:118px;width:240px">Lorem ipsum dolor sit amet, consec tetur adipiscing elit.</p>
    <span class="read-more" style="left:226px;top:176px">Read More</span>
  </article>
</section>

<footer class="site-footer">
  <div class="foot-brand">Copper Lantern<br><span class="accent">Vending Services</span></div>
  <div class="foot-divider" style="left:324px"></div><div class="foot-divider grey" style="left:324px"></div>
  <div class="foot-divider" style="left:538px"></div><div class="foot-divider grey" style="left:538px"></div>
  <div class="foot-divider" style="left:778px"></div><div class="foot-divider grey" style="left:778px"></div>

  <h4 class="foot-head" style="left:364px">Quick Links</h4>
  <ul class="quick-links"><li>Home</li><li>About Us</li><li>Vending Machines</li><li>Resources</li><li>Contact Us</li></ul>

  <h4 class="foot-head" style="left:573px">Contact Info</h4>
  <div class="contact-item" style="top:112px">
    <svg width="11" height="15" viewBox="0 0 12 16"><path fill="#e3230f" d="M6 0a6 6 0 0 0-6 6c0 4.5 6 10 6 10s6-5.5 6-10a6 6 0 0 0-6-6zm0 8.5A2.5 2.5 0 1 1 6 3.5a2.5 2.5 0 0 1 0 5z"/></svg>
    <div class="label">Address:</div><div class="val">465, Lorum Ipsum Dolore,<br>United States</div>
  </div>
  <div class="contact-item" style="top:192px">
    <svg width="12" height="12" viewBox="0 0 24 24"><path fill="#e3230f" d="M6.6 10.8a15.1 15.1 0 0 0 6.6 6.6l2.2-2.2c.3-.3.7-.4 1-.2 1.1.4 2.3.6 3.6.6.6 0 1 .4 1 1V20c0 .6-.4 1-1 1A17 17 0 0 1 3 4c0-.6.4-1 1-1h3.5c.6 0 1 .4 1 1 0 1.3.2 2.5.6 3.6.1.3 0 .7-.2 1z"/></svg>
    <div class="label">Phone:</div><div class="val">+1 (305) 555 0142</div>
  </div>
  <div class="contact-item" style="top:252px">
    <svg width="13" height="11" viewBox="0 0 24 18"><rect width="24" height="18" rx="2" fill="#e3230f"/><path d="M2 3l10 7 10-7" stroke="#1d1d1d" stroke-width="2" fill="none"/></svg>
    <div class="label">Email:</div><div class="val">info@copperlantern.co</div>
  </div>

  <h4 class="foot-head" style="left:805px">Join Newsletter</h4>
  <div class="newsletter"><span>Email Address</span><b>JOIN NOW</b></div>
  <div class="foot-socials"><div class="soc fill"></div><div class="soc"></div><div class="soc"></div><div class="soc"></div></div>

  <div class="chat"><svg width="22" height="18" viewBox="0 0 22 18" fill="#fff"><path d="M2 1h12a2 2 0 0 1 2 2v6a2 2 0 0 1-2 2H7l-4 3v-3H2a2 2 0 0 1-2-2V3a2 2 0 0 1 2-2z"/><path d="M18 6h2a2 2 0 0 1 2 2v5a2 2 0 0 1-2 2h-1v3l-4-3h-5a2 2 0 0 1-2-2v-1h6a4 4 0 0 0 4-4z"/></svg></div>
  <div class="foot-rule"></div>
  <p class="copyright">© 2023 <b style="font-weight:500">COPPER LANTERN VENDING SERVICES</b> &nbsp;|&nbsp; All Rights Reserved</p>
</footer>

</body>
</html>
```